Postcard Design

My company name is Perch Skyward. We offer FAA approved drone photography and videography for real estate marketing. Our target demographic customer base is Realtors, Real Estate Brokerages (their Brokers in Charge "BIC's and owners), Builders and Developers. There are currently only two FAA approved drone operators in the greater Raleigh "Lattice" area. Our website is www.PerchSkyward-demo.com. All current packages and pricing are featured there. Our prices are extremely affordable by design to make drone marketing available to all types of real estate rather than just the luxury markets. I have a Perch Lattice logo for our real estate business but I'd like to modify it a bit to replace "Homes Colective" with "Aerial" and have an image of a ZQR Osprey V underneath Perch (black with the same effect as the word "Lattice". I'll provide examples of my photography as well as the logo I'd like modified. I'd like this post card to be eye catching and include a 25% off promotion off all our packages through January, 2016. The postcard can be two sided. Our motto is "Let Perch Skyward take your real estate marketing to new heights". I prefer a clean contemporary feel rather than the cartoonish cluttered look.

Industry/Entity Type

Real Estate

```html
<!DOCTYPE html>
<html lang="en">
<head>
<meta charset="utf-8">
<title>Perch Skyward – Postcard</title>
<link href="https://fonts.googleapis.com/css2?family=Roboto+Condensed:ital,wght@0,400;0,700;1,300;1,400&family=Open+Sans:ital,wght@0,400;0,700;1,400&display=swap" rel="stylesheet">
<style>
  :root{
    --header-top:#2c4d6b;
    --header-mid:#4f7593;
    --header-bottom:#6d8fa9;
    --band-blue:#3e6584;
    --band-blue-dark:#28475f;
    --accent-blue:#2aa7e6;
    --light-blue:#5cc3f2;
    --rule-grey:#b9b9b9;
    --text-dark:#2b2b2b;
    --text-body:#3d3d3d;
    --slate:#4a4a4c;
    --white:#ffffff;
    --ink:#111111;
  }
  *{box-sizing:border-box;margin:0;padding:0}
  html,body{width:773px;height:1200px;overflow:hidden;background:#fff}
  .postcard{position:relative;width:773px;height:1200px;overflow:hidden;font-family:"Open Sans",Arial,sans-serif}

  .masthead{position:absolute;left:0;top:0;width:773px;height:173px;
    background:linear-gradient(180deg,var(--header-top) 0%,var(--header-mid) 55%,var(--header-bottom) 100%)}
  .brand{position:absolute;left:34px;top:62px;display:flex;align-items:center;gap:14px}
  .brand-mark{width:22px;height:22px;background:var(--white)}
  .brand-name{font-family:"Roboto Condensed",Arial,sans-serif;font-weight:700;font-size:44px;color:var(--white);letter-spacing:0.5px;line-height:1}
  .contact{position:absolute;left:369px;top:52px;font-family:"Roboto Condensed",Arial,sans-serif;font-size:20px;line-height:29px;color:var(--white)}

  .hero{position:absolute;left:0;top:173px;width:773px;height:333px;
    background:
      radial-gradient(ellipse at 75% 45%,rgba(235,235,240,.85) 0 12%,transparent 26%),
      linear-gradient(180deg,#9aa6ae 0%,#8c8a6f 30%,#a8683a 55%,#6f4a2c 78%,#50483d 100%)}

  .tagline-band{position:absolute;left:0;top:506px;width:773px;height:63px;
    background:linear-gradient(180deg,var(--band-blue) 0%,var(--band-blue-dark) 100%);
    display:flex;align-items:center;justify-content:center;
    font-family:"Roboto Condensed",Arial,sans-serif;font-weight:700;font-size:37px;color:var(--white);letter-spacing:.3px}
  .tagline-band .accent{color:var(--accent-blue);margin-left:9px}

  .benefits{position:absolute;left:0;top:569px;width:773px;height:371px;background:var(--white)}
  .rule-h{position:absolute;left:14px;right:14px;top:200px;height:2px;background:var(--rule-grey)}
  .rule-v{position:absolute;left:385px;top:10px;bottom:4px;width:2px;background:var(--rule-grey)}
  .benefit{position:absolute;width:350px}
  .benefit.tl{left:24px;top:52px}
  .benefit.tr{left:402px;top:52px}
  .benefit.bl{left:24px;top:226px}
  .benefit.br{left:402px;top:226px}
  .benefit-head{display:flex;align-items:flex-end;gap:6px;height:48px}
  .tick{width:50px;height:48px;flex:none}
  .benefit-title{font-family:"Roboto Condensed",Arial,sans-serif;line-height:1.05}
  .benefit-title strong{display:block;font-weight:700;font-size:21px;color:var(--text-dark)}
  .benefit-title em{display:block;font-weight:400;font-style:italic;font-size:19px;color:var(--text-dark)}
  .benefit-body{margin-top:9px;font-size:12px;font-weight:700;line-height:17px;color:var(--text-body);text-align:justify}

  .promise{position:absolute;left:0;top:940px;width:773px;height:180px;background:var(--slate);text-align:center;padding-top:12px}
  .promise-lead{font-family:"Roboto Condensed",Arial,sans-serif;font-weight:700;font-size:25px;line-height:30px;color:var(--light-blue)}
  .promise-copy{margin-top:4px;font-family:"Roboto Condensed",Arial,sans-serif;font-style:italic;font-weight:300;font-size:29px;line-height:33px;color:var(--white)}
  .promise-offer{margin-top:10px;font-family:"Roboto Condensed",Arial,sans-serif;font-weight:700;font-size:19px;line-height:24px;color:var(--light-blue)}
  .promise-offer .web{color:var(--white);font-weight:400;margin-left:10px}

  .call-bar{position:absolute;left:0;top:1120px;width:773px;height:80px;
    background:linear-gradient(180deg,#7f9fb7 0%,#5a7f9c 100%);
    display:flex;flex-direction:column;align-items:center;justify-content:center;
    font-family:"Roboto Condensed",Arial,sans-serif;color:var(--ink)}
  .call-number{font-weight:700;font-size:33px;line-height:36px}
  .motto{font-style:italic;font-weight:400;font-size:15px;line-height:20px;color:var(--white)}
</style>
</head>
<body>
<div class="postcard">
  <header class="masthead">
    <div class="brand">
      <span class="brand-mark"></span>
      <span class="brand-name">Perch Skyward</span>
    </div>
    <div class="contact">
      <div>1420 Larkmoor Lane, Fernbrook, NC 27599</div>
      <div>Phone : 919-555-0147</div>
      <div>Hello@PerchLattice-demo.com</div>
    </div>
  </header>

  <div class="hero" role="img" aria-label="Photograph of a camera drone hovering above a wooded home with autumn trees"></div>

  <div class="tagline-band">A NEW PERSPECTIVE ON<span class="accent">YOUR LISTINGS</span></div>

  <section class="benefits">
    <div class="rule-h"></div>
    <div class="rule-v"></div>

    <article class="benefit tl">
      <div class="benefit-head">
        <svg class="tick" viewBox="0 0 58 56" aria-hidden="true"><rect x="3" y="16" width="36" height="36" fill="#fff" stroke="#2a5f8f" stroke-width="3"/><path d="M10 32 L20 44 L54 4 L22 36 Z" fill="#2aa7e6"/></svg>
        <div class="benefit-title"><strong>Impress</strong><em>Potential Clients</em></div>
      </div>
      <p class="benefit-body">With hundreds of homes available on the market you need to stand out...give buyers the "wow" factor.. Aerial photography and images will set your listings apart</p>
    </article>

    <article class="benefit tr">
      <div class="benefit-head">
        <svg class="tick" viewBox="0 0 58 56" aria-hidden="true"><rect x="3" y="16" width="36" height="36" fill="#fff" stroke="#2a5f8f" stroke-width="3"/><path d="M10 32 L20 44 L54 4 L22 36 Z" fill="#2aa7e6"/></svg>
        <div class="benefit-title"><strong>Impress</strong><em>Potential Buyers</em></div>
      </div>
      <p class="benefit-body">Showcasing your listing so that buyers see all angles and in the context of the neighborhood makes the buyer feel more connected to your home. This leads to faster sales closer to your asking price.</p>
    </article>

    <article class="benefit bl">
      <div class="benefit-head">
        <svg class="tick" viewBox="0 0 58 56" aria-hidden="true"><rect x="3" y="16" width="36" height="36" fill="#fff" stroke="#2a5f8f" stroke-width="3"/><path d="M10 32 L20 44 L54 4 L22 36 Z" fill="#2aa7e6"/></svg>
        <div class="benefit-title"><strong>Stand Out to</strong><em>Potential Clients</em></div>
      </div>
      <p class="benefit-body">Only a small percentage of Realtors are using arial drone technology. In fact there are only 2 companies that have the government mandated FAA certificate for flying drones in the Raleigh Lattice. Your listings will stand out and you will gain the edge over your competition.</p>
    </article>

    <article class="benefit br">
      <div class="benefit-head">
        <svg class="tick" viewBox="0 0 58 56" aria-hidden="true"><rect x="3" y="16" width="36" height="36" fill="#fff" stroke="#2a5f8f" stroke-width="3"/><path d="M10 32 L20 44 L54 4 L22 36 Z" fill="#2aa7e6"/></svg>
        <div class="benefit-title"><strong>Stand Out to</strong><em>Potential Buyers</em></div>
      </div>
      <p class="benefit-body">Our low prices allow you to market modestly priced homes as if they were Million dollar homes. You can offer your clients premium marketing at a reasonable cost.</p>
    </article>
  </section>

  <section class="promise">
    <p class="promise-lead">Take your listings to the next level....</p>
    <p class="promise-copy">A well marketed home gets more offers... in less time.<br>Agents who's listings sell quickly...get more listings.</p>
    <p class="promise-offer">25% OFF all packages through January, 2016<span class="web">www.PerchSkyward-demo.com</span></p>
  </section>

  <footer class="call-bar">
    <div class="call-number">919-555-0147</div>
    <div class="motto">Let Perch Skyward take your real estate marketing to new heights</div>
  </footer>
</div>
</body>
</html>
```